Lantern Walk! A website showcasing who I am as a person

Lantern Walk started out as idea for me to better myself as a person and work on small projects that would help me grow as a person. Now I want to build a website showcasing "Lantern Walk." I want the website to showcase who I am and how I have grown both professionally and personally. I can build the raw code of the website on my own but I am not really much of a designer. I am looking for a design where I can write and post blogs, articles and share my thoughts. A little about myself and the ideas and interests that I want to share
What is Lantern Walk
Who I am
Background - Professional
Brand Marketing
Email Automation
Hiking
Rock Climbing
Traveling
Exercising and Transformation
"Personal Thoughts"
Hopefully this is enough information to get people started on some designs.
Industry/Entity Type
Work
Number of Pages Required
3 page

```html
<!DOCTYPE html>
<html lang="en">
<head>
<meta charset="utf-8">
<title>Lantern Walk — Mara</title>
<link href="https://fonts.googleapis.com/css2?family=Roboto:wght@400;500;700&family=Playfair+Display:wght@700&family=Rufina:wght@400;700&display=swap" rel="stylesheet">
<style>
:root{
  --orange:#f26a10;
  --teal:#3b8a7f;
  --blue:#2b6cb0;
  --grey-bar:#666666;
  --ink:#1e1e1e;
  --text:#555555;
  --muted:#777777;
  --panel:#f2f2f2;
  --line:#e2e2e2;
  --footer:#3a3a3a;
}
*{box-sizing:border-box;margin:0;padding:0}
html,body{width:1200px;height:2936px;overflow:hidden}
body{position:relative;background:#fff;font-family:"Roboto",Arial,sans-serif;color:var(--text)}

/* Header */
.hero{position:absolute;left:0;top:0;width:1200px;height:411px;
  background:radial-gradient(ellipse at 55% 40%,#e2dfdf 0%,#cfcbcb 55%,#c2bebe 100%)}
.brand{position:absolute;left:112px;top:30px;font:700 19px/22px "Roboto",sans-serif;color:#111;letter-spacing:-.3px}
.search{position:absolute;left:880px;top:25px;width:208px;height:33px;border-radius:17px;background:#fff;
  display:flex;align-items:center;padding-left:14px;gap:8px;font-size:13px;color:#444}
.portrait{position:absolute;left:626px;top:0;width:300px;height:411px;
  background:linear-gradient(180deg,#6b4a38 0%,#8c6a56 35%,#e9e6e4 60%,#f4f2f1 100%);
  border-radius:120px 120px 0 0}
.hi{position:absolute;left:112px;top:118px;width:92px;height:92px}
.hi span{position:absolute;left:0;top:0;width:92px;height:92px;display:flex;align-items:center;justify-content:center;
  font:700 44px/1 "Playfair Display",serif;color:#fff}
.intro-name{position:absolute;left:120px;top:222px;font:700 64px/1 "Rufina",serif;color:var(--teal)}
.intro-role{position:absolute;left:124px;top:293px;font:400 34px/1 "Rufina",serif;color:#222}

/* Posts */
.posts{position:absolute;left:112px;top:460px;width:641px}
.post{height:577px}
.meta{display:flex;align-items:center;gap:6px;height:20px;font-size:12px;color:var(--muted)}
.meta .author{color:var(--orange);font-weight:700}
.meta .gap{width:14px}
.post-title{margin-top:10px;font:400 20px/24px "Roboto",sans-serif;color:var(--ink)}
.post-image{margin-top:18px;height:307px}
.excerpt{margin-top:18px;font-size:13px;line-height:21px;color:var(--text)}
.more{margin-top:17px;height:33px;border-top:2px solid var(--line);border-bottom:2px solid var(--line);
  display:flex;align-items:center;justify-content:center;gap:4px;font:700 11px/1 "Roboto",sans-serif;color:#333;letter-spacing:.3px}

.img-meeting{background:linear-gradient(135deg,#b98b64 0%,#8a6a58 40%,#4a5a6e 100%)}
.img-email{background:linear-gradient(135deg,#1b2a3f 0%,#4a3c30 45%,#d6b27a 70%,#9a5a4a 100%)}
.img-travel{background:linear-gradient(180deg,#9fb8cf 0%,#8a8775 40%,#5e5a44 100%)}
.img-climb{background:linear-gradient(180deg,#7fb0e0 0%,#bcd6ee 55%,#8f7a68 100%)}

/* Pagination */
.pager{position:absolute;left:256px;top:2770px;display:flex;gap:8px}
.pager a{height:34px;min-width:34px;padding:0 12px;border:2px solid #ddd;border-radius:17px;display:flex;align-items:center;justify-content:center;
  font-size:12px;color:#555;text-decoration:none}
.pager a.num{padding:0;width:34px}
.pager a.current{border-color:var(--orange);color:var(--orange)}

/* Sidebar */
.sidebar{position:absolute;left:779px;top:462px;width:309px}
.widget{background:var(--panel);padding:0 18px 18px 20px;border-top:4px solid transparent}
.widget + .widget{margin-top:35px}
.widget-title{display:flex;align-items:center;gap:10px;margin:0 -18px 0 -2px;height:32px;
  font:700 19px/1 "Rufina",serif;color:#222}
.widget-title::after{content:"";flex:1;height:12px;background:var(--bar)}
.about{--bar:var(--orange)}
.recent{--bar:var(--teal)}
.archives{--bar:var(--blue)}
.social{--bar:var(--grey-bar)}
.widget p{margin-top:10px;font-size:12.5px;line-height:20px;color:var(--text)}
.recent ul{list-style:none;margin-top:8px}
.recent li{padding:12px 0 13px;border-bottom:1px solid var(--line)}
.recent li:last-child{border-bottom:0;padding-bottom:0}
.recent .t{font-size:14px;line-height:20px;color:#333}
.recent .d{font-size:12px;color:var(--muted);margin-top:2px}
.recent .d b{color:var(--orange)}
.subscribe{background:var(--teal);border:3px solid #2f7268;padding:0 18px 18px 18px;--bar:#5ea79c}
.subscribe .widget-title{color:#fff;margin:0 -18px 0 0}
.subscribe .field{margin-top:14px;height:34px;background:#fff;border-radius:2px;display:flex;align-items:center;padding-left:12px;font-size:12.5px;color:#777}
.subscribe .btn{margin-top:8px;height:34px;background:var(--orange);border-radius:2px;display:flex;align-items:center;justify-content:center;
  font:700 12.5px/1 "Roboto",sans-serif;color:#fff}
.archives ul{list-style:none;margin-top:14px}
.archives li{font-size:12.5px;line-height:24px;color:var(--text);display:flex;align-items:center;gap:6px}
.archives li::before{content:"";border:3px solid transparent;border-left:4px solid #999;border-right:0}
.social-row{display:flex;gap:6px;margin-top:10px}
.social-row span{width:31px;height:31px;border-radius:50%}

/* Footer */
.footer{position:absolute;left:0;top:2847px;width:1200px;height:89px;background:var(--footer);color:#a5a5a5;font-size:12px}
.footer nav{position:absolute;left:0;width:100%;top:25px;display:flex;justify-content:center;gap:8px}
.footer nav i{font-style:normal;color:#777}
.footer .copy{position:absolute;width:100%;top:51px;text-align:center}
.to-top{position:absolute;left:1051px;top:24px;width:36px;height:39px;background:#5a5a5a;border-radius:2px;
  display:flex;flex-direction:column;align-items:center;justify-content:center;font:700 10px/1 "Roboto",sans-serif;color:#ddd;gap:3px}
</style>
</head>
<body>

<header class="hero">
  <div class="brand">Lantern Walk</div>
  <div class="search">
    <svg width="14" height="14" viewBox="0 0 14 14"><circle cx="6" cy="6" r="4.5" fill="none" stroke="#333" stroke-width="1.6"/><line x1="9.3" y1="9.3" x2="13" y2="13" stroke="#333" stroke-width="1.8"/></svg>
    Search
  </div>
  <div class="hi">
    <svg width="92" height="92" viewBox="0 0 92 92"><path d="M46 2a44 44 0 1 1-30 76L4 90l6-18A44 44 0 0 1 46 2z" fill="#f26a10"/></svg>
    <span>Hi.</span>
  </div>
  <h1 class="intro-name">I'm Mara</h1>
  <p class="intro-role">Business Professional</p>
  <div class="portrait" role="img" aria-label="Portrait photo of Mara, a business professional in a white blouse"></div>
</header>

<main class="posts">
  <article class="post">
    <div class="meta">
      <svg width="12" height="12" viewBox="0 0 12 12"><circle cx="6" cy="3.5" r="3" fill="#888"/><path d="M0 12c0-4 3-5.5 6-5.5s6 1.5 6 5.5z" fill="#888"/></svg>
      By <span class="author">Owen Hale</span><span class="gap"></span>
      <svg width="12" height="12" viewBox="0 0 12 12"><rect x="0.5" y="1.5" width="11" height="10" fill="none" stroke="#888"/><rect x="0.5" y="1.5" width="11" height="3" fill="#888"/></svg>
      28 March 2017<span class="gap"></span>
      <svg width="12" height="12" viewBox="0 0 12 12"><path d="M0 0h6l6 6-6 6-6-6z" fill="#888"/><circle cx="3" cy="3" r="1.2" fill="#fff"/></svg>
      Brand Marketing
    </div>
    <h2 class="post-title">The standard Lorem Ipsum passage used since the awesome as well as explain to you how all this mistaken idea</h2>
    <div class="post-image img-meeting" role="img" aria-label="Photo of a team gathered around a table in a brainstorming meeting"></div>
    <p class="excerpt">Class aptent taciti sociosqu ad litora torquent per conubia nostra, per inceptos himenaeos. Mauris in erat justo. Nullam ac urna eu felis dapibus condimentum sit amet a augue. Sed non neque elit. Sed uimperdiet ut aliquam massa nisl quis neque. Suspendisse in orci enim.</p>
    <div class="more">CONTINUE READING <svg width="6" height="8" viewBox="0 0 6 8"><path d="M0 0l6 4-6 4z" fill="#333"/></svg></div>
  </article>

  <article class="post">
    <div class="meta">
      <svg width="12" height="12" viewBox="0 0 12 12"><circle cx="6" cy="3.5" r="3" fill="#888"/><path d="M0 12c0-4 3-5.5 6-5.5s6 1.5 6 5.5z" fill="#888"/></svg>
      By <span class="author">Owen Hale</span><span class="gap"></span>
      <svg width="12" height="12" viewBox="0 0 12 12"><rect x="0.5" y="1.5" width="11" height="10" fill="none" stroke="#888"/><rect x="0.5" y="1.5" width="11" height="3" fill="#888"/></svg>
      28 March 2017<span class="gap"></span>
      <svg width="12" height="12" viewBox="0 0 12 12"><path d="M0 0h6l6 6-6 6-6-6z" fill="#888"/><circle cx="3" cy="3" r="1.2" fill="#fff"/></svg>
      Email Automation
    </div>
    <h2 class="post-title">The standard Lorem Ipsum passage used since the awesome as well as explain to you how all this mistaken idea</h2>
    <div class="post-image img-email" role="img" aria-label="Photo of hands typing on a laptop with glowing envelope icons floating above"></div>
    <p class="excerpt">Class aptent taciti sociosqu ad litora torquent per conubia nostra, per inceptos himenaeos. Mauris in erat justo. Nullam ac urna eu felis dapibus condimentum sit amet a augue. Sed non neque elit. Sed uimperdiet ut aliquam massa nisl quis neque. Suspendisse in orci enim.</p>
    <div class="more">CONTINUE READING <svg width="6" height="8" viewBox="0 0 6 8"><path d="M0 0l6 4-6 4z" fill="#333"/></svg></div>
  </article>

  <article class="post">
    <div class="meta">
      <svg width="12" height="12" viewBox="0 0 12 12"><circle cx="6" cy="3.5" r="3" fill="#888"/><path d="M0 12c0-4 3-5.5 6-5.5s6 1.5 6 5.5z" fill="#888"/></svg>
      By <span class="author">Owen Hale</span><span class="gap"></span>
      <svg width="12" height="12" viewBox="0 0 12 12"><rect x="0.5" y="1.5" width="11" height="10" fill="none" stroke="#888"/><rect x="0.5" y="1.5" width="11" height="3" fill="#888"/></svg>
      28 March 2017<span class="gap"></span>
      <svg width="12" height="12" viewBox="0 0 12 12"><path d="M0 0h6l6 6-6 6-6-6z" fill="#888"/><circle cx="3" cy="3" r="1.2" fill="#fff"/></svg>
      Traveling
    </div>
    <h2 class="post-title">The standard Lorem Ipsum passage used since the awesome as well as explain to you how all this mistaken idea</h2>
    <div class="post-image img-travel" role="img" aria-label="Photo of a hiker with a backpack resting above a mountain valley"></div>
    <p class="excerpt">Class aptent taciti sociosqu ad litora torquent per conubia nostra, per inceptos himenaeos. Mauris in erat justo. Nullam ac urna eu felis dapibus condimentum sit amet a augue. Sed non neque elit. Sed uimperdiet ut aliquam massa nisl quis neque. Suspendisse in orci enim.</p>
    <div class="more">CONTINUE READING <svg width="6" height="8" viewBox="0 0 6 8"><path d="M0 0l6 4-6 4z" fill="#333"/></svg></div>
  </article>

  <article class="post">
    <div class="meta">
      <svg width="12" height="12" viewBox="0 0 12 12"><circle cx="6" cy="3.5" r="3" fill="#888"/><path d="M0 12c0-4 3-5.5 6-5.5s6 1.5 6 5.5z" fill="#888"/></svg>
      By <span class="author">Owen Hale</span><span class="gap"></span>
      <svg width="12" height="12" viewBox="0 0 12 12"><rect x="0.5" y="1.5" width="11" height="10" fill="none" stroke="#888"/><rect x="0.5" y="1.5" width="11" height="3" fill="#888"/></svg>
      28 March 2017<span class="gap"></span>
      <svg width="12" height="12" viewBox="0 0 12 12"><path d="M0 0h6l6 6-6 6-6-6z" fill="#888"/><circle cx="3" cy="3" r="1.2" fill="#fff"/></svg>
      Rock Climbing
    </div>
    <h2 class="post-title">The standard Lorem Ipsum passage used since the awesome as well as explain to you how all this mistaken idea</h2>
    <div class="post-image img-climb" role="img" aria-label="Photo of a climber hanging from a rock overhang against a blue sky"></div>
    <p class="excerpt">Class aptent taciti sociosqu ad litora torquent per conubia nostra, per inceptos himenaeos. Mauris in erat justo. Nullam ac urna eu felis dapibus condimentum sit amet a augue. Sed non neque elit. Sed uimperdiet ut aliquam massa nisl quis neque. Suspendisse in orci enim.</p>
    <div class="more">CONTINUE READING <svg width="6" height="8" viewBox="0 0 6 8"><path d="M0 0l6 4-6 4z" fill="#333"/></svg></div>
  </article>
</main>

<nav class="pager">
  <a href="#">◂ Prev</a>
  <a href="#" class="num current">01</a>
  <a href="#" class="num">02</a>
  <a href="#" class="num">03</a>
  <a href="#" class="num">05</a>
  <a href="#" class="num">06</a>
  <a href="#">Next ▸</a>
</nav>

<aside class="sidebar">
  <section class="widget about">
    <h3 class="widget-title">About Us</h3>
    <p>Class aptent taciti sociosqu ad litora torquent per conubia nostra, per inceptos himenaeos. Mauris in erat justo. Nullam ac urna eu felis dapibus condimentum sit amet a augue. Sed non neque elit.</p>
  </section>

  <section class="widget recent">
    <h3 class="widget-title">Recent Posts</h3>
    <ul>
      <li><div class="t">The standard Lorem Ipsum passage used since the awesome</div><div class="d">By <b>Owen Hale</b> | 28 March 2017</div></li>
      <li><div class="t">The standard Lorem Ipsum passage used since the awesome</div><div class="d">By <b>Owen Hale</b> | 28 March 2017</div></li>
      <li><div class="t">The standard Lorem Ipsum passage used since the awesome</div><div class="d">By <b>Owen Hale</b> | 28 March 2017</div></li>
      <li><div class="t">The standard Lorem Ipsum passage used since the awesome</div><div class="d">By <b>Owen Hale</b> | 28 March 2017</div></li>
    </ul>
  </section>

  <section class="widget subscribe">
    <h3 class="widget-title">Subecribe</h3>
    <div class="field">Email Address</div>
    <div class="btn">SUBSCRIBE</div>
  </section>

  <section class="widget archives">
    <h3 class="widget-title">Archives</h3>
    <ul>
      <li>January 2017</li>
      <li>February 2017</li>
      <li>March 2017</li>
      <li>April 2017</li>
      <li>May 2017</li>
    </ul>
  </section>

  <section class="widget social">
    <h3 class="widget-title">Social</h3>
    <div class="social-row">
      <span style="background:#3b5b98" role="img" aria-label="Social profile link"></span>
      <span style="background:#2aa3e0" role="img" aria-label="Social profile link"></span>
      <span style="background:#3f6f95" role="img" aria-label="Social profile link"></span>
      <span style="background:#c9202d" role="img" aria-label="Social profile link"></span>
      <span style="background:#1b74b3" role="img" aria-label="Social profile link"></span>
    </div>
  </section>
</aside>

<footer class="footer">
  <nav>
    <span>About Us</span><i>•</i><span>Contact</span><i>•</i><span>Site Map</span><i>•</i><span>Privacy Policy</span><i>•</i><span>Terms &amp; Conditions</span><i>•</i><span>Accessibility</span>
  </nav>
  <div class="copy">© 2017 Company Name.</div>
  <div class="to-top"><svg width="8" height="5" viewBox="0 0 8 5"><path d="M0 5l4-5 4 5z" fill="#ddd"/></svg>TOP</div>
</footer>

</body>
</html>
```